The Hollow Lantern with Dov Ransbury

Create Podcast Art for Podwave. My podcast is about overcoming adversities.

Everyone's adversity is different and there's no one-size-fits-all solution, but when you hear someone's else's story of resilience and add a little salt to it, you can find the inspiration you need to write a new ending to your struggle.

Maybe you're going through something right now and you're afraid:

● You won't be successful
● People are talking behind your back
● You'll never get the help you need
● You're not a good husband or wife
● Your child is out of control and you'll never get through to him or her
● There isn't a light at the end of your tunnel
● You'll never get your finances out of the red
● Your spouse won't ever see things your way
● The world is never gonna change

Every story we tell on The Hollow Lantern podcast challenges those thoughts, because everyday people going through everyday stuff just like you show us otherwise.

This podcast is for you. And, it's different.

Most interviews I do, I try to go on location and interview in person.

You might not see us together on the screen,
but you'll sense the raw sincerity and closeness of a side-by-side interview through your speakers.

The colors I have chosen below are close to the website colors. If you need a better view of that go here http://www.dovransbury-example.com

I've attached two pictures for the podcast. I'm not sure which one to use just yet so I put them both here to see what i created by your great people!

Target Market(s)

People who are currently going through an Advesirty or have been through one. 28 - 40 age group.

Colors
ec1f27
ffffff
000000
fbee3e

Requirements
Must have
• Eye appeal and The title "The Hollow Lantern" with Dov Ransbury
• HAS to be stand-out, and it HAS to give a great first impression.
Nice to have
• The colors I have chosen are close to the website colors.

```html
<!DOCTYPE html>
<html lang="en">
<head>
<meta charset="utf-8">
<title>The Hollow Lantern with Dov Ransbury</title>
<link rel="stylesheet" href="https://fonts.googleapis.com/css2?family=Open+Sans:wght@700;800&display=swap">
<style>
  :root {
    --brand-red: #ec1f27;
    --white: #ffffff;
    --wall-pink: #c8587a;
    --wall-pink-light: #d7739a;
    --ground-grey: #b9b3b0;
    --brick-orange: #d0664a;
    --sweater-grey: #8a8d97;
    --denim-blue: #2d4f86;
  }
  html, body {
    margin: 0;
    padding: 0;
    overflow: hidden;
    background: var(--white);
  }
  .cover {
    position: relative;
    width: 1200px;
    height: 1200px;
    overflow: hidden;
    font-family: "Open Sans", Arial, sans-serif;
  }
  .backdrop {
    position: absolute;
    inset: 0;
    background: linear-gradient(180deg,
      var(--wall-pink-light) 0%,
      var(--wall-pink) 55%,
      #c56a86 70%,
      var(--ground-grey) 75%,
      var(--brick-orange) 82%,
      #b8553e 100%);
  }
  .host-photo {
    position: absolute;
    left: 480px;
    top: 40px;
    width: 720px;
    height: 1160px;
    background: linear-gradient(180deg,
      rgba(138,141,151,0) 0%,
      rgba(138,141,151,0.85) 22%,
      var(--sweater-grey) 60%,
      var(--denim-blue) 85%,
      #24406e 100%);
    border-radius: 260px 0 0 0;
  }
  .title {
    position: absolute;
    left: 36px;
    top: 200px;
    margin: 0;
    color: var(--white);
    font-weight: 800;
    letter-spacing: -0.035em;
    line-height: 196px;
  }
  .title span { display: block; }
  .title .title-lead { font-size: 196px; }
  .title .title-main { font-size: 232px; }
  .host-band {
    position: absolute;
    left: 0;
    top: 810px;
    width: 670px;
    height: 60px;
    background: var(--brand-red);
    color: var(--white);
    font-weight: 700;
    font-size: 44px;
    line-height: 60px;
    padding-left: 38px;
    box-sizing: border-box;
    white-space: nowrap;
  }
</style>
</head>
<body>
  <main class="cover">
    <div class="backdrop" role="img" aria-label="Pink painted brick wall with a stack of old red bricks in the foreground"></div>
    <div class="host-photo" role="img" aria-label="Podcast host seated, wearing a grey sweater over a checked shirt and jeans"></div>
    <h1 class="title">
      <span class="title-lead">The</span>
      <span class="title-main">Hollow</span>
      <span class="title-main">Lantern</span>
    </h1>
    <div class="host-band">WITH DOV RANSBURY</div>
  </main>
</body>
</html>
```